Meridel Advisory & Coaching Collective Web Site Design

Help!

We have started designing and building a Web site to promote and sell training services to HR managers. But we are not very good designers. In fact, we stink.

We have a logo.

We have most of the content (more or less) and the site architecture. But we have put together a pretty lousy look and feel.

Take a look: http://brightlowpath.example/vortalindex.html

What we'd like is a Web 3.0 type design - clean, simple, modern looking. Some sites we admire:

pinvale.example
trelosk.example
skivorn.example
quibbledot.example
morpa.example

We have access to stock photography, some of which we've used on the site we've built so far. You can use those and others. But keep it simple.

Target Market(s)

Professional HR managers in larger companies

Requirements
Must have
• Use our logo and a color scheme based off of it. Logo file uploaded.

Need to see home page and examples of secondary pages, based on site currently online.

```html
<!DOCTYPE html>
<html lang="en">
<head>
<meta charset="utf-8">
<title>Meridel Collective – Home</title>
<link href="https://fonts.googleapis.com/css2?family=Ubuntu:wght@300;400;500&display=swap" rel="stylesheet">
<style>
:root{
  --navy:#2b3d8f;
  --blue:#0c6fc0;
  --sky:#1a9be0;
  --sky-soft:#3aa6e6;
  --orange:#f7941d;
  --orange-deep:#f07c10;
  --orange-light:#fdbb2f;
  --ink:#222;
  --muted:#6a6a6a;
  --rule:#e3e8ee;
  --paper:#fff;
}
*{margin:0;padding:0;box-sizing:border-box}
html,body{width:1079px;height:1200px;overflow:hidden}
body{font-family:"Ubuntu",sans-serif;background:var(--paper);position:relative;color:var(--ink)}
.abs{position:absolute}
.backdrop{left:0;top:0;width:1079px;height:382px;background:var(--navy)}
.backdrop-stripe{left:0;top:382px;width:1079px;height:11px;background:var(--sky)}
.page{left:83px;top:0;width:914px;height:1167px;background:linear-gradient(#fff 0,#fff 700px,#f1f2f4 100%)}
.header-curve{left:500px;top:0;width:497px;height:133px}
.brand{left:110px;top:38px;font-size:25px;font-weight:400;color:var(--ink);display:flex;align-items:center;gap:7px;white-space:nowrap}
.brand-dot{width:14px;height:14px;border-radius:50%;background:var(--blue)}
.brand small{font-size:14px;color:var(--blue)}
.tagline{left:83px;top:94px;width:417px;height:35px;background:linear-gradient(var(--orange-light),var(--orange));color:#fff;font-size:16px;padding:7px 14px;border-radius:0 0 30px 0;white-space:nowrap}
.login{left:617px;top:14px;display:flex;align-items:center;gap:10px;color:#fff;font-size:14px}
.field{width:140px;height:26px;border:1px solid #7cc4f0;background:var(--sky);border-radius:3px;font-size:11px;color:#cfe9fa;padding:6px 10px}
.go{width:32px;height:26px;background:var(--navy);color:#fff;font-size:14px;text-align:center;padding-top:4px;border-radius:2px}
.login-links{left:790px;top:62px;font-size:11px;color:#fff;word-spacing:2px}
.search{left:751px;top:93px;width:238px;height:31px;background:#fff;border:1px solid #cfdbe6;font-size:11px;color:#bbb;padding:9px 15px}
.search svg{position:absolute;right:8px;top:6px}
.nav{left:83px;top:133px;width:914px;height:45px;background:linear-gradient(#f7f7f7,#dedede);display:flex;font-size:16px;color:#444}
.nav span{padding:13px 4px;border-right:1px solid #d0d0d0;text-align:center;white-space:nowrap}
.nav .current{background:var(--blue);color:#fff;width:78px}
.feature{top:192px;width:275px;height:189px;border:4px solid var(--orange);background:linear-gradient(135deg,#c9cdd2,#7a8390)}
.feature.f2{background:linear-gradient(135deg,#8a8f96,#2f3642)}
.feature.f3{background:linear-gradient(135deg,#d4d0c8,#5b6470)}
.feature-caption{position:absolute;left:0;bottom:14px;width:205px;height:30px;background:linear-gradient(90deg,var(--orange),rgba(247,148,29,.85));color:#fff;font-size:19px;padding:3px 20px;clip-path:polygon(0 0,100% 0,88% 100%,0 100%);white-space:nowrap}
.tooltip{left:144px;top:367px;width:214px;height:34px;background:var(--sky-soft);color:#fff;font-size:12px;text-align:center;line-height:14px;padding-top:3px;border-radius:3px}
.tooltip-label{left:18px;top:313px;width:53px;height:50px;background:#fff;color:#d0312d;font-size:12px;text-align:center;padding-top:17px}
.tabs-band{left:83px;top:400px;width:914px;height:50px;background:linear-gradient(var(--orange-light),var(--orange-deep))}
.tab{top:412px;width:143px;height:38px;border-radius:8px 8px 0 0;background:linear-gradient(#fec33c,var(--orange));color:#333;font-size:19px;text-align:center;padding-top:10px;box-shadow:0 -1px 2px rgba(0,0,0,.1)}
.section-title{left:104px;top:471px;font-size:20px;color:var(--blue)}
.section-rule{left:83px;top:491px;width:540px;height:1px;background:linear-gradient(90deg,var(--blue),rgba(12,111,192,0))}
.copy{left:112px;width:520px;font-size:11px;line-height:15.3px;color:#333}
.card{background:#fff;border:1px solid var(--rule);border-radius:8px}
.sidebar{left:735px;top:463px;width:246px;height:473px}
.sidebar h2{font-size:23px;font-weight:400;color:var(--blue);padding:20px 0 0 20px;height:76px}
.sidebar li{list-style:none;font-size:11px;color:var(--muted);padding:3px 18px 4px 30px;line-height:15px;margin-bottom:2px}
.sidebar li.active{background:var(--sky);color:#fff;position:relative;margin:0 -1px 6px;padding:6px 18px 6px 31px}
.sidebar li.active::before{content:"";position:absolute;left:12px;top:14px;border-left:8px solid #fff;border-top:5px solid transparent;border-bottom:5px solid transparent}
.panel{left:107px;top:716px;width:600px;height:220px}
.panel h2{position:absolute;font-size:22px;font-weight:400;color:var(--blue);top:12px}
.quote{position:absolute;left:20px;top:80px;width:280px;text-align:center;font-size:11px;line-height:15.3px;color:#333}
.qmark{position:absolute;font-size:30px;color:var(--orange);font-weight:500}
.divider{position:absolute;left:300px;top:52px;width:1px;height:150px;background:var(--rule)}
.solutions{position:absolute;left:320px;top:55px;list-style:none}
.solutions li{font-size:11px;color:var(--muted);height:20.5px;display:flex;align-items:center;gap:9px}
.footer-rule{left:88px;top:957px;width:904px;height:2px;background:var(--blue)}
.footer h3{position:absolute;font-size:19px;font-weight:400;color:var(--blue);top:978px}
.fcol{font-size:11px;line-height:15.3px;color:#333}
.fsep{top:1008px;width:1px;height:145px;background:#dcdcdc}
.social{left:116px;top:1014px;list-style:none}
.social li{display:flex;align-items:center;gap:16px;font-size:14px;color:#555;height:29px;margin-bottom:1px}
.social i{display:block;width:24px;height:24px;background:var(--blue);border-radius:3px}
.social li:nth-child(2) i{background:var(--navy)}
.social li:nth-child(3) i{background:var(--sky)}
.res{left:575px;top:1016px;list-style:none}
.res li{font-size:11px;color:var(--muted);height:20.5px}
.copyright{left:0;top:1182px;width:1079px;text-align:center;font-size:11px;color:#444}
</style>
</head>
<body>
<div class="abs backdrop"></div>
<div class="abs backdrop-stripe"></div>
<div class="abs page"></div>

<svg class="abs header-curve" viewBox="0 0 497 133" aria-hidden="true">
  <path d="M20 133 C 20 40, 40 0, 110 0 L497 0 L497 133 Z" fill="#0c6fc0"/>
  <path d="M101 0 L497 0 L497 80 L115 80 Q101 80 101 66 Z" fill="#2a9de3"/>
</svg>

<div class="abs brand"><span class="brand-dot"></span>Meridel Collective <small>…for Norvask HR Guild</small></div>
<div class="abs tagline">Generational Tools &amp; Training for HR Professionals</div>

<div class="abs login">Login <div class="field">Username</div><div class="field">Password</div><div class="go">Go</div></div>
<div class="abs login-links">Forgot Password? &nbsp; Not a Member?</div>
<div class="abs search">Search our site…
  <svg width="20" height="20" viewBox="0 0 20 20" aria-hidden="true"><circle cx="8" cy="8" r="5.5" fill="none" stroke="#555" stroke-width="2"/><line x1="12" y1="12" x2="18" y2="18" stroke="#555" stroke-width="3"/></svg>
</div>

<nav class="abs nav">
  <span class="current">Home</span><span style="width:89px">About us</span><span style="width:81px">Gen 101</span><span style="width:99px">Gen Gaps</span><span style="width:112px">Strategies</span><span style="width:102px">Resources</span><span style="width:95px">Training</span><span style="width:92px">Discuss</span><span style="width:73px">Tools</span><span style="width:93px;border:0">Contact us</span>
</nav>

<div class="abs feature" style="left:108px" role="img" aria-label="Photo of a smiling colleague with a team at an office table"><div class="feature-caption">Generations 101</div></div>
<div class="abs feature f2" style="left:404px" role="img" aria-label="Photo of a business team in a meeting"><div class="feature-caption">Generations Gaps</div></div>
<div class="abs feature f3" style="left:701px" role="img" aria-label="Photo of colleagues discussing around a table"><div class="feature-caption">Gen Strategies</div></div>

<div class="abs tooltip">Learn who the generations<br>are and why they matter.</div>
<div class="abs tooltip-label">Tooltips</div>

<div class="abs tabs-band"></div>
<div class="abs tab" style="left:115px">Resources</div>
<div class="abs tab" style="left:272px">Training</div>
<div class="abs tab" style="left:427px">Tools</div>
<div class="abs tab" style="left:583px">Discuss</div>

<h1 class="abs section-title" style="font-weight:400">Home</h1>
<div class="abs section-rule"></div>

<p class="abs copy" style="top:513px">Why our client never get tired of our services why our client never get tired of our servicesrft<br>Why our client never get tired of our services why our client never get tired of our servicesffh<br>Why our client never get tired of our services why our client never get tired of our serviceshffh<br>Why our client never get tired of our services why our client never get tired of our services<br>Why our client never get ti</p>
<p class="abs copy" style="top:599px">Why our client never get tired of our services why our client never get tired of our servicesrft<br>Why our client never get tired of our services why our client never get tired of our servicesffh<br>Why our client never get tired of our services why our client never get tired of our serviceshffh<br>Why our client never get tired of our services why our client never get tired of our services<br>Why our client never get ti</p>

<aside class="abs card sidebar">
  <h2>Why Choose us?</h2>
  <ul>
    <li>Why Our Company is the best from all?</li>
    <li class="active">Why our client never get tired of our Services?</li>
    <li>Why Our Company is the best from all?</li>
    <li>Why our client never get tired of our Services?</li>
    <li>Why Our Company is the best from all?</li>
    <li>Why our client never get tired of our Services?</li>
    <li>Why Our Company is the best from all?</li>
    <li>Why our client never get tired of our Services?</li>
    <li>Why Our Company is the best from all?</li>
    <li>Why our client never get tired of our Services?</li>
    <li style="margin-top:8px">Why Our Company is the best from all?</li>
    <li>Why our client never get tired of our Services?</li>
  </ul>
</aside>

<section class="abs card panel">
  <h2 style="left:20px">Testimonies</h2>
  <div class="qmark" style="left:22px;top:44px">“</div>
  <p class="quote">Why our client never get tired of our services<br>why our client never get tired of our servicesrft<br>Why our client never get tired of our services<br>why our client never get tired of our servicesffh<br>Why our client never get tired of our services<br>why our client never get tired of our serviceshffh</p>
  <div class="qmark" style="left:272px;top:170px">”</div>
  <div class="divider"></div>
  <h2 style="left:314px">Our Solutions</h2>
  <ul class="solutions">
    <li><svg width="16" height="12" viewBox="0 0 16 12" aria-hidden="true"><path d="M1 6 L6 10 L15 1" fill="none" stroke="#f07c10" stroke-width="2.5"/></svg>Our New Resources here is a great idea</li>
    <li><svg width="16" height="12" viewBox="0 0 16 12" aria-hidden="true"><path d="M1 6 L6 10 L15 1" fill="none" stroke="#f07c10" stroke-width="2.5"/></svg>Our New Resources here is a great idea</li>
    <li><svg width="16" height="12" viewBox="0 0 16 12" aria-hidden="true"><path d="M1 6 L6 10 L15 1" fill="none" stroke="#f07c10" stroke-width="2.5"/></svg>Our New Resources here is a great idea</li>
    <li><svg width="16" height="12" viewBox="0 0 16 12" aria-hidden="true"><path d="M1 6 L6 10 L15 1" fill="none" stroke="#f07c10" stroke-width="2.5"/></svg>Our New Resources here is a great idea</li>
    <li><svg width="16" height="12" viewBox="0 0 16 12" aria-hidden="true"><path d="M1 6 L6 10 L15 1" fill="none" stroke="#f07c10" stroke-width="2.5"/></svg>Our New Resources here is a great idea</li>
    <li><svg width="16" height="12" viewBox="0 0 16 12" aria-hidden="true"><path d="M1 6 L6 10 L15 1" fill="none" stroke="#f07c10" stroke-width="2.5"/></svg>Our New Resources here is a great idea</li>
    <li><svg width="16" height="12" viewBox="0 0 16 12" aria-hidden="true"><path d="M1 6 L6 10 L15 1" fill="none" stroke="#f07c10" stroke-width="2.5"/></svg>Our New Resources here is a great idea</li>
  </ul>
</section>

<div class="abs footer-rule"></div>
<footer class="footer">
  <h3 style="left:106px">Connect with us</h3>
  <h3 style="left:345px">Contact us?</h3>
  <h3 style="left:557px">Our Resources</h3>
  <h3 style="left:770px">About us?</h3>
  <ul class="abs social">
    <li><i></i>Like our page</li>
    <li><i></i>Keep touch with us</li>
    <li><i></i>Tweet with us</li>
    <li style="margin-top:3px"><i></i>Network with us</li>
  </ul>
  <div class="abs fsep" style="left:325px"></div>
  <p class="abs fcol" style="left:358px;top:1016px">Get in touch with us<br>with our e-mail and<br>numbers.<br><br>info@calderpoint.example<br>+1 (555) 010-2277<br>+1 (555) 010-2278<br><br>Address: 8, Tolvane Street.</p>
  <div class="abs fsep" style="left:538px"></div>
  <ul class="abs res">
    <li>Our New Resources here</li><li>Our New Resources here</li><li>Our New Resources here</li><li>Our New Resources here</li><li>Our New Resources here</li><li>Our New Resources here</li><li>Our New Resources here</li>
  </ul>
  <div class="abs fsep" style="left:747px"></div>
  <p class="abs fcol" style="left:771px;top:1016px">Get in touch with us<br>with our e-mail and<br>numbers.<br><br>info@calderpoint.example<br>+1 (555) 010-2277<br>+1 (555) 010-2278<br><br>Address: 8, Tolvane Street.</p>
</footer>
<p class="abs copyright">Copyright Meridel Collective, 2011, All Right Reserved.</p>
</body>
</html>
```